Product presentation and placement brochure

I have cardiovascular exercise equipment (treadmill, bikes, eliptical trainers, etc.) that have a coin timers attached that allow use of this exercise equipment using coins. I want to market to apartment buildings, swimming pools, training gyms, etc. We want them to partner with us by allowing us to place our equipment in their locations. Their residents would get new equipment to use, they use a coin to get so much time. The apartment building doesn't pay anything precharge us workspace, but they will get a 10 - 20% of all the revenue that flows through the machines in their building.This brochure needs to clearly display our equipment, how the residents can use it, the ease of the relationship between us and the apartment building, and how they will make money with no investment and no commitment.I would, like the brochure to look artistic, not so mechanical.

Target Market(s)

Large apartment buildings, Public swimming pools, training studios, gyms, etc.

Font styles to use
Serif

Colors

Designer to choose colors to be used in the design.

Requirements
Must have
• The basic wording for the brochure. Must have English and Chinese.
• Vela Pulse Machine Brochure
• 霖森健身器材指南
• We will pay YOU to let us provide YOU with commercial cardiovascular equipment.
• 我們付你錢來讓我們提供你有氧器材
• We supply cardio equipment to your residents at no cost to you. In fact, we will pay you! Please take a moment to look at our brochure and see how we can work with you and your homeowners association to bring the latest in fitness technology to your building, and we’ll pay you for it.
• 在不花費你任何金錢的情況下, 我們提供有氧器材給你的住戶。甚至我們付你錢!請看我們的手冊來了解我們如何能和你跟社區管理委員會合作, 把最新的健身器材介紹到你的大樓, 並且帶給你收益。
• Our machines are all equipped with patented coin operated technology. If your residents would like to have the luxury of quality exercise, they may insert dollars for minutes.
• 我們的器材皆具備專利通過投幣式設計。如果你的住戶想要享有高品質運動, 他們可以投幣來取得運動時間。
• By the 10th of every month, we will pay 15% of all revenue collected for the previous month, minus taxes, to you or your homeowners association, whichever you choose.
• 每個月10號, 我們將付你或社區管理委員會前一個月百分之十五不含稅的收入。
• Why it is so easy:
• 1. We provide the equipment at no cost to you.
• 2. We pay for shipping and installation.
• 3. Month-to-month agreement, no commitment from you.
• 4. Removal with 30 days notice, no questions asked.
• 5. We conduct all repairs and regular maintenance.
• 6. We will pay you from the revenue collected!
• 為什麼超簡單:
• 1. 不花你一毛錢, 器材我們提供。
• 2. 運送費跟安裝費, 全數我們支付。
• 3. 以一個月為一期, 不用長期保證。
• 4. 30天移出通知, 不需任何理由。
• 5. 所有器材維修, 我們負責。
• 6. 器材收益,我們分享!
• As easy as 1, 2, 3!
• 簡單有如1, 2, 3!
• STEP 1
• We have several different machine types that will motivate your residents to exercise:
• 1. Treadmill (photo and stats.)
• 2. Recumbent Bike (photo and stats.)
• 3. Regular Seated Bike (photo and stats.)
• 4. Elliptical trainer (photo and stats.)
• Replace old equipment, broken equipment, or just place new equipment next to your old equipment.
• 第一步
• 我們有多種有氧器材可讓住戶更有動力運動:
• 1. 跑步機
• 2. 臥式腳踏車
• 3. 直立式腳踏車
• 4. 橢圓機
• 替換原有老舊的運動器材, 或是直接放一台新的器材在原有器材的旁邊。
• After meeting with you and determining you and your residents needs, we will decide how many and of what types of equipment you would like in your exercise room.
• 在和你會面並且評估你和住戶的需求後, 我們會決定你想要的器材種類和數量。
• STEP 2
• We will deliver and install the equipment, in a suitable location that you choose. All at no cost to you!
• 第二步
• 我們將器材運送到你選擇的合適場所並安裝。不需任何費用!
• Step 3
• 第三步
• Make your residents healthy and happy by letting them use any of the equipment, for as long as they like, at their leisure.
• 住戶可盡情使用任何器材, 讓住戶健康又開心。
• Photo Steps on how to use equipment
• 0. 2. 3.
• We would be happy to answer any of your questions and give you a free consultation on how you can utilize this service to bring affordable fitness to your residents, while creating a revenue stream for you or your homeowners association.
• 我們很樂意回答任何問題並免費提供諮詢:如何有效利用此服務以帶給住戶能負擔的健身運動, 且同時創造收益給你或社區管理委員會。
• For more Information, please:
• visit our website at:
• call:
• Email:
• 更多資訊請:
• 拜訪我們的網站:
• 電話聯絡:
• 傳送電子郵件:
• Tomas Kelder
• Ruth Okonji
• Vela Pulse Fitness
• Manager of Marketing and English Translation
• Ph: +17605550187
• LINE ID: quietotter
• Email: quiet-otter@mailvessa.com
Nice to have
• I would like it to be have a high tech artsy feel. I don't want the haredline industrial.

```html
<!DOCTYPE html>
<html lang="en">
<head>
<meta charset="utf-8">
<title>Vela Pulse Fitness – Brochure Cover Spread</title>
<link rel="stylesheet" href="https://fonts.googleapis.com/css2?family=Open+Sans:wght@400;600;700;800&family=Noto+Sans+TC:wght@500;800&display=swap">
<style>
  :root{
    --canvas:#ececec;
    --paper:#ffffff;
    --mist:#e4e4e4;
    --mist-dark:#cfcfcf;
    --ink:#141414;
    --ink-soft:#2a2a2a;
    --olive:#9c9a2c;
    --olive-deep:#6f6d1c;
    --volt:#f2e21c;
    --text-light:#f4f4f4;
    --text-dim:#bdbdbd;
    --text-dark:#222222;
  }
  *{box-sizing:border-box;margin:0;padding:0}
  html,body{width:900px;height:1200px;overflow:hidden;background:var(--canvas)}
  body{font-family:"Open Sans",Arial,sans-serif;position:relative}
  .spread{position:absolute;left:20px;top:296px;width:860px;height:608px;display:flex;box-shadow:0 12px 30px rgba(0,0,0,.18)}
  .page{position:relative;width:430px;height:608px;overflow:hidden;background:var(--paper)}
  .page-art{position:absolute;inset:0;width:100%;height:100%}

  /* back cover */
  .contact{position:absolute;left:110px;top:92px;width:170px;text-align:center;color:var(--text-dark)}
  .contact-title{display:inline-block;background:var(--volt);color:var(--ink);font-weight:600;font-size:12px;padding:4px 26px;border-radius:10px;margin-bottom:18px}
  .contact-item{display:flex;flex-direction:column;align-items:center;margin-bottom:16px;font-size:11px;font-weight:600;letter-spacing:.2px}
  .contact-icon{width:18px;height:18px;margin-bottom:5px}
  .follow{position:absolute;right:40px;bottom:70px;display:flex;align-items:center;gap:6px;color:var(--text-light);font-size:11px;font-weight:700}
  .social-dot{width:12px;height:12px;border-radius:50%;background:var(--text-light)}
  .back-note{position:absolute;right:28px;bottom:22px;width:240px;color:var(--text-dim);font-size:7.5px;line-height:1.4;text-align:right}

  /* front cover */
  .brand{position:absolute;left:30px;top:42px;display:flex;align-items:center;gap:10px;color:var(--ink)}
  .brand-dot{width:46px;height:46px;border-radius:50%;background:var(--ink)}
  .brand-name{font-weight:800;font-size:14px;letter-spacing:.6px;text-transform:uppercase;line-height:1.35}
  .brand-name span{display:block;font-family:"Noto Sans TC","Open Sans",sans-serif;font-weight:800;font-size:13px;letter-spacing:4px}
  .headline{position:absolute;left:40px;bottom:78px;color:var(--text-light);text-transform:uppercase;line-height:1.05}
  .headline-lead{display:block;color:var(--volt);font-weight:800;font-size:22px}
  .headline-main{display:block;font-weight:800;font-size:17px}
  .headline-sub{display:block;font-weight:700;font-size:9.5px;margin-top:3px;letter-spacing:.2px}
  .web{position:absolute;left:40px;bottom:44px;width:220px;padding-top:8px;border-top:1px dotted var(--text-dim);color:var(--text-light);font-size:10px}
  .web b{color:var(--volt);font-weight:700}
</style>
</head>
<body>
  <main class="spread">
    <!-- Back cover -->
    <section class="page page-back">
      <svg class="page-art" viewBox="0 0 430 608" aria-hidden="true">
        <defs>
          <linearGradient id="mistBack" x1="0" y1="0" x2="1" y2="1">
            <stop offset="0" stop-color="#ededed"/><stop offset="1" stop-color="#d4d4d4"/>
          </linearGradient>
        </defs>
        <rect width="430" height="608" fill="#ffffff"/>
        <path d="M22 0 H430 V360 Q280 470 22 520 Z" fill="url(#mistBack)"/>
        <path d="M430 392 Q260 495 0 556 V608 H430 Z" fill="#9c9a2c"/>
        <path d="M430 410 Q260 515 0 580 V608 H430 Z" fill="#141414"/>
      </svg>
      <div class="contact">
        <div class="contact-title">Get In Touch</div>
        <div class="contact-item">
          <svg class="contact-icon" viewBox="0 0 18 18"><circle cx="9" cy="9" r="9" fill="#141414"/><path d="M6 5l2 0 1 2.5-1.2 1a5 5 0 0 0 2.7 2.7l1-1.2L14 11v2c-4 .3-8.3-4-8-8z" fill="#f2e21c"/></svg>
          (+886) 0970555218
        </div>
        <div class="contact-item">
          <svg class="contact-icon" viewBox="0 0 18 18"><circle cx="9" cy="9" r="9" fill="#141414"/><circle cx="9" cy="9" r="4.5" fill="none" stroke="#f2e21c" stroke-width="1.2"/><path d="M4.5 9h9M9 4.5v9" stroke="#f2e21c" stroke-width="1"/></svg>
          www.velapulsefitness.com
        </div>
        <div class="contact-item">
          <svg class="contact-icon" viewBox="0 0 18 18"><circle cx="9" cy="9" r="9" fill="#141414"/><path d="M9 14s-3.5-3.8-3.5-6a3.5 3.5 0 0 1 7 0c0 2.2-3.5 6-3.5 6z" fill="#f2e21c"/><circle cx="9" cy="8" r="1.2" fill="#141414"/></svg>
          3F, No. 42 Linsen Rd. Tainan
        </div>
      </div>
      <div class="follow">Follow Us On: <i class="social-dot"></i><i class="social-dot"></i><i class="social-dot"></i></div>
      <p class="back-note">Our machines are all equipped with patented coin operated technology. If your residents would like to have the luxury of quality exercise, they may insert dollars for minutes.</p>
    </section>

    <!-- Front cover -->
    <section class="page page-front">
      <svg class="page-art" viewBox="0 0 430 608">
        <defs>
          <linearGradient id="mistFront" x1="0" y1="0" x2="1" y2="1">
            <stop offset="0" stop-color="#e8e8e8"/><stop offset="1" stop-color="#d2d2d2"/>
          </linearGradient>
          <linearGradient id="photoTone" x1="0" y1="0" x2="1" y2="1">
            <stop offset="0" stop-color="#8a8468"/><stop offset=".45" stop-color="#c9bf5a"/><stop offset="1" stop-color="#6a6454"/>
          </linearGradient>
        </defs>
        <rect width="430" height="608" fill="url(#mistFront)"/>
        <rect y="240" width="430" height="368" fill="#9c9a2c"/>
        <path role="img" aria-label="Photo of a member stretching in a yellow-walled exercise room beside a Chinese-language banner" d="M430 24 Q260 112 92 262 L92 338 L430 418 Z" fill="url(#photoTone)"/>
        <path d="M380 0 H430 V24 Q260 112 92 262 L0 340 V298 Q190 120 380 0 Z" fill="#ffffff"/>
        <path d="M40 332 L430 414 V426 L40 344 Z" fill="#f2e21c"/>
        <path d="M0 392 L430 474 V608 H0 Z" fill="#141414"/>
        <path d="M250 418 L430 452 V476 Z" fill="#6f6d1c"/>
      </svg>
      <div class="brand">
        <i class="brand-dot"></i>
        <div class="brand-name">Vela Pulse Fitness<span>霖森健身中心</span></div>
      </div>
      <h1 class="headline">
        <span class="headline-lead">We Will Pay You</span>
        <span class="headline-main">To Let Us Provide You</span>
        <span class="headline-sub">With Commercial Cardiovascular Equipment</span>
      </h1>
      <div class="web">www.<b>velapulsefitness</b>.com</div>
    </section>
  </main>
</body>
</html>
```